Brookhaven Business Card

I would like to re-design my company business card. I have my main company logo (Brookhaven) which must remain unchanged and I also have a number of product brands which I would like to also show on the card in some way. The corporate company colors are Blue and Orange, see pantone colors on file. However, it is not necessary to use these colors thoroughout. I am ok with grey tones etc...

Target Market(s)

Trade Business

Industry/Entity Type

Furniture

Contact Information for Business Card

Needs to incorporate Brookhaven as the main Logo. The Torvel and Kandrel product brands within the company. These can be on the back of the card.

Font styles to use
Sans Serif

Colors
0355a3
f37122

Requirements
Must have
• Marco Velditch
• COO (Global)
• Brookhaven Pacific Holdings Inc. (4371)
• Level 3, 47 Harlow Street, Melbourne VIC 3000 Australia
• Tel: +61 3 9481 2736 Mobile: +61 427 586 204
• e-mail: marco@brookhaven-au.example
• web: www.brookhaven-au.example
Nice to have
• Should be a corporate
Should not have
• No images of furniture

```html
<!DOCTYPE html>
<html lang="en">
<head>
<meta charset="utf-8">
<title>Brookhaven Business Card</title>
<link rel="stylesheet" href="https://fonts.googleapis.com/css2?family=Ubuntu:wght@400;500;700&display=swap">
<style>
  :root {
    --backdrop: #3a302b;
    --card: #1f1f21;
    --card-back: #161617;
    --emboss: #2c2c2e;
    --blue: #0355a3;
    --blue-bright: #1a6fd0;
    --orange: #f37122;
    --text-light: #c9c9c9;
    --white: #ffffff;
  }
  * { margin: 0; padding: 0; box-sizing: border-box; }
  html, body {
    width: 1200px;
    height: 716px;
    overflow: hidden;
  }
  body {
    background: var(--backdrop);
    font-family: "Ubuntu", sans-serif;
    position: relative;
  }
  .card {
    position: absolute;
    width: 500px;
    height: 286px;
    border-radius: 4px;
    box-shadow: 0 12px 30px rgba(0,0,0,0.45);
    overflow: hidden;
  }
  /* Back of card */
  .card-back {
    left: 70px;
    top: 215px;
    background: var(--card-back);
    display: flex;
    align-items: center;
    justify-content: center;
    gap: 18px;
  }
  .card-back .brand-square {
    width: 58px;
    height: 58px;
    border-radius: 10px;
    border: 3px solid var(--emboss);
  }
  .card-back .brand-name {
    font-size: 52px;
    font-weight: 700;
    color: var(--emboss);
    letter-spacing: -0.5px;
  }
  /* Front of card */
  .card-front {
    left: 630px;
    top: 215px;
    background: var(--card);
  }
  .front-brand {
    position: absolute;
    left: 26px;
    top: 24px;
    display: flex;
    align-items: center;
    gap: 12px;
  }
  .front-brand .brand-square {
    width: 30px;
    height: 30px;
    border-radius: 5px;
    background: var(--orange);
  }
  .front-brand .brand-name {
    font-size: 30px;
    font-weight: 500;
    color: var(--blue-bright);
  }
  .person {
    position: absolute;
    left: 26px;
    top: 72px;
  }
  .person-name {
    font-size: 17px;
    font-weight: 500;
    color: var(--blue-bright);
  }
  .person-title {
    font-size: 10px;
    color: var(--text-light);
    margin-top: 3px;
  }
  .company {
    font-size: 11px;
    font-weight: 500;
    color: var(--blue-bright);
    margin-top: 6px;
  }
  .contact-list {
    position: absolute;
    left: 26px;
    top: 142px;
    list-style: none;
    font-size: 10.5px;
    color: var(--text-light);
    line-height: 16px;
  }
  .contact-list li {
    display: flex;
    align-items: center;
    gap: 7px;
  }
  .contact-list svg {
    width: 10px;
    height: 10px;
    fill: var(--orange);
    flex: none;
  }
  .address {
    position: absolute;
    left: 26px;
    top: 212px;
    font-size: 10.5px;
    line-height: 15px;
    color: var(--text-light);
  }
  .mark-block {
    position: absolute;
    right: 34px;
    top: 52px;
    width: 150px;
    height: 150px;
    background: var(--orange);
  }
  .product-brands {
    position: absolute;
    right: 24px;
    bottom: 20px;
    display: flex;
    align-items: center;
    gap: 22px;
  }
  .product-kandrel {
    display: flex;
    align-items: center;
    gap: 6px;
    font-size: 14px;
    font-weight: 700;
    color: var(--white);
  }
  .product-kandrel .dot {
    width: 18px;
    height: 18px;
    border-radius: 50%;
    background: var(--white);
  }
  .product-torvel {
    font-size: 15px;
    font-weight: 700;
    color: var(--white);
  }
</style>
</head>
<body>

  <section class="card card-back" aria-label="Card back">
    <div class="brand-square"></div>
    <div class="brand-name">Brookhaven</div>
  </section>

  <section class="card card-front" aria-label="Card front">
    <div class="front-brand">
      <div class="brand-square"></div>
      <div class="brand-name">Brookhaven</div>
    </div>

    <div class="person">
      <div class="person-name">Marco Velditch</div>
      <div class="person-title">COO (Global)</div>
      <div class="company">Brookhaven Pacific Holdings Inc. (4371)</div>
    </div>

    <ul class="contact-list">
      <li>
        <svg viewBox="0 0 10 10" aria-hidden="true"><path d="M2 0h2l1 2.5-1.3 1a5 5 0 0 0 2.8 2.8l1-1.3L10 6v2a2 2 0 0 1-2 2A8 8 0 0 1 0 2a2 2 0 0 1 2-2z"/></svg>
        +61 3 9481 2736
      </li>
      <li>
        <svg viewBox="0 0 10 10" aria-hidden="true"><rect x="2" y="0" width="6" height="10" rx="1"/><rect x="3" y="1.2" width="4" height="6.5" fill="#1f1f21"/></svg>
        +61 427 586 204
      </li>
      <li>
        <svg viewBox="0 0 10 10" aria-hidden="true"><circle cx="5" cy="5" r="5"/><path d="M0 5h10M5 0c-2 2.5-2 7.5 0 10M5 0c2 2.5 2 7.5 0 10" stroke="#1f1f21" stroke-width="0.8" fill="none"/></svg>
        www.brookhaven-au.example
      </li>
      <li>
        <svg viewBox="0 0 10 10" aria-hidden="true"><rect x="0" y="1.5" width="10" height="7" rx="0.8"/><path d="M0.5 2l4.5 3.5L9.5 2" stroke="#1f1f21" stroke-width="0.9" fill="none"/></svg>
        marco@brookhaven-au.example
      </li>
    </ul>

    <div class="address">
      Level 3, 47 Harlow Street,<br>
      Melbourne VIC 3000 Australia
    </div>

    <div class="mark-block"></div>

    <div class="product-brands">
      <div class="product-kandrel"><span class="dot"></span>Kandrel</div>
      <div class="product-torvel">Torvel</div>
    </div>
  </section>

</body>
</html>
```